依頼詳細
販促の一環としてフリーペーパーに広告を出稿します。(A4・1ページ)
つきましてはA4広告1枚の制作をお願い致します。
【サイズ】 天地297mm × 左右210mm

■出稿にあたり意識すること

・ゴルフウェアのレンタルサービスがあるということを知ってもらうこと
・サービスの利便性を簡潔に訴えること(※◎の訴求は必須です。)
◎送料無料  ◎洗濯クリーニング不要  ◎1泊2日/¥2,100~
△添付の訴求バナー①内容(※できれば訴求したいです。)
・「初回無料キャンペーン」「フォトコンテスト」を実施中ということ

【添付】
・弊社ロゴ
・サービス訴求バナー
(送料無料)(洗濯・クリーニング不要)(1泊2日/¥2,100~)(訴求バナー①)
・参考例(2点)
・当方が制作したもの
記載項目
A4広告の制作にあたり添付バナーの使用は問いません。
(添付バナーの使用、ご自身で制作どちらも可です。)
サイズ
A4
ページ数
片面
希望イメージ
シンプル 複雑
単色 カラフル
暗い 明るい
日常 高級
遊び心 厳粛
未来的 伝統的
女性的 男性的
希望する色
納品ファイル
• 高解像度JPG (.jpg)
• イラストレーター形式 (.ai)
補足説明
■ 選んだ理由

ゴルフ+レンタル が良く伝わる素敵なデザインのため

■ 提案者全員のお礼・コメント

この度はご提案誠にありがとうございました。
今後もコンペ形式にてご依頼をしますので機会がございましたら宜しくお願い致します。

```html
<!DOCTYPE html>
<html lang="ja">
<head>
<meta charset="utf-8">
<title>FAIRWAY rent – golf wear rental</title>
<link rel="stylesheet" href="https://fonts.googleapis.com/css2?family=Roboto+Mono:wght@700&family=Noto+Sans+JP:wght@400;500;700;900&display=swap">
<style>
  :root {
    --yellow: #fbf58a;
    --white: #ffffff;
    --pink: #fbe3ea;
    --ink: #1c1c1c;
    --green: #2f9a3c;
    --accent: #e8607d;
  }
  * { margin: 0; padding: 0; box-sizing: border-box; }
  html, body { width: 849px; height: 1200px; overflow: hidden; background: var(--white); }
  .ad {
    position: relative;
    width: 849px;
    height: 1200px;
    overflow: hidden;
    background: var(--white);
    font-family: "Noto Sans JP", sans-serif;
    color: var(--ink);
  }
  .top-band {
    position: absolute; left: 0; top: 0;
    width: 100%; height: 583px;
    background: var(--yellow);
  }
  .brand {
    position: absolute; left: 26px; top: 22px;
    display: flex; align-items: center; gap: 10px;
    font-family: "Noto Sans JP", sans-serif;
    font-weight: 900;
    font-size: 34px;
    color: var(--green);
    letter-spacing: 0.5px;
  }
  .brand-dot {
    width: 16px; height: 16px; border-radius: 50%;
    background: var(--green);
  }
  .headline {
    position: absolute; left: 0; top: 355px;
    width: 100%;
    text-align: center;
    font-family: "Roboto Mono", monospace;
    font-weight: 700;
    font-size: 104px;
    line-height: 128px;
    letter-spacing: 6px;
    color: var(--ink);
  }
  .intro {
    position: absolute; left: 0; top: 812px;
    width: 100%;
    text-align: center;
    font-size: 15px;
    line-height: 30px;
    font-weight: 500;
    letter-spacing: 0.5px;
  }
  .intro .service-name { font-weight: 700; font-size: 17px; }
  .bottom-band {
    position: absolute; left: 0; top: 1033px;
    width: 100%; height: 167px;
    background: var(--pink);
  }
  .points {
    position: absolute; left: 154px; top: 1058px;
    display: flex; gap: 0;
  }
  .point {
    width: 116px; height: 116px; border-radius: 50%;
    background: var(--white);
    display: flex; flex-direction: column; align-items: center; justify-content: center;
    text-align: center;
    margin-right: -3px;
  }
  .point-label {
    font-family: "Roboto Mono", monospace;
    font-size: 10px; color: var(--accent);
    margin-bottom: 4px;
  }
  .point-text { font-size: 13px; font-weight: 700; line-height: 17px; }
  .point-text.large { font-size: 19px; line-height: 24px; }
  .point-text small { display: block; font-size: 11px; font-weight: 500; }
  .campaigns {
    position: absolute; left: 548px; top: 1076px;
    list-style: none;
    font-size: 14px; line-height: 42px; font-weight: 500;
  }
  .campaigns li::before { content: "・"; }
</style>
</head>
<body>
  <main class="ad">
    <div class="top-band"></div>

    <div class="brand"><span class="brand-dot"></span>FAIRWAY rent</div>

    <h1 class="headline">golf<br>wear<br>rental</h1>

    <p class="intro">
      「購入するには高すぎる…だけどお洒落なゴルフウェアが着たい！」<br>
      そんなお悩みを解決するのがゴルフウェアレンタルサービス<br>
      <span class="service-name">“フェアウェイレント”</span>です。
    </p>

    <div class="bottom-band"></div>

    <div class="points">
      <div class="point">
        <span class="point-label">point 1</span>
        <span class="point-text"><small>1泊2日</small>¥2,100〜</span>
      </div>
      <div class="point">
        <span class="point-label">point 2</span>
        <span class="point-text"><small>洗濯・クリーニング</small>不要!</span>
      </div>
      <div class="point">
        <span class="point-label">point 3</span>
        <span class="point-text large">送料無料</span>
      </div>
    </div>

    <ul class="campaigns">
      <li>初回無料キャンペーン実施中</li>
      <li>「フォトコンテスト」実施中</li>
    </ul>
  </main>
</body>
</html>
```